Brook Medical Needs a PowerPoint Design

Brook Medical needs a PowerPoint template developed for use during presentations by our marketing department. Brook offers Medical specialty services to family physicians throughout Calgary. At Brook we pride ourselves on our commitment to our patients as well as having very short wait times and convenient locations spread throughout the communities. We offer services in Pulmonary Diagnostics as well as sleep apnea assessment and treatment. Consults from medical specialties such as Respirology, Physiatry, Internal Medicine, Occupational Medicine, Pediatric Infectious Disease, and alergy are also available.

***Please note we are not looking for you to build a presentation we just want the design of the slides for us to add content as needed****

We require an updated powerpoint template that we can use in a range of situations such as during marketing presentations or professional educational events. We would like a design that is modern and unique. We would like the mountain theme built into the design elements of the slide deck

We require a whole slide deck (Title slide; etc) for the Brook Medical Group as well as a body slide for our sleep division.

Our usual font is ArnoPro Semi Bold

Our Websites: brookairway.example brookrestclinic.example

Closest pantone color for Brook’s purple is PMS 814 2X

Target Market(s)

Physicians, medical professionals

Industry/Entity Type

Medical

Font styles to use
Other font styles liked:
• ArnoPro Semi Bold

Requirements
Must have
• Similar look and feel to sleep and medical slide
Nice to have
• Mountain design built into deck.
Should not have
• large actual images of mountains.

```html
<!DOCTYPE html>
<html lang="en">
<head>
<meta charset="utf-8">
<title>Brook Medical – Print Slide</title>
<link href="https://fonts.googleapis.com/css2?family=Archivo:wdth,wght@125,400;125,500&family=Open+Sans:wght@400&display=swap" rel="stylesheet">
<style>
  :root {
    --purple: #7e4a91;
    --purple-soft: #b99bc4;
    --purple-mist: #e7dcea;
    --ink: #1d1d1d;
    --paper: #ffffff;
    --slate: #4a7d9a;
    --green: #5bb58a;
    --orange: #f39a2e;
    --red: #e84a3f;
    --grid: #d9c4de;
  }
  * { margin: 0; padding: 0; box-sizing: border-box; }
  html, body { width: 849px; height: 1200px; overflow: hidden; background: var(--paper); }
  .slide {
    position: relative; width: 849px; height: 1200px; overflow: hidden;
    background: linear-gradient(90deg, var(--purple-soft) 0%, var(--purple-mist) 18%, var(--paper) 38%);
  }
  .side-artwork {
    position: absolute; left: 0; top: 170px; width: 250px; height: 760px;
    background: radial-gradient(ellipse at 40% 45%, rgba(126,74,145,.35), rgba(126,74,145,0) 70%);
  }
  .side-dots { position: absolute; left: 10px; top: 170px; display: grid; gap: 10px; }
  .side-dots span { width: 16px; height: 12px; background: rgba(255,255,255,.7); }
  .brand {
    position: absolute; left: 16px; top: 20px; display: flex; align-items: center; gap: 10px;
    font-family: "Archivo", sans-serif; font-weight: 500; font-size: 20px; color: var(--purple);
  }
  .brand-square { width: 26px; height: 26px; background: var(--purple); }
  .agenda {
    position: absolute; left: 210px; top: 34px; list-style: none;
    font-family: "Archivo", sans-serif; font-stretch: 125%; font-weight: 400;
    font-size: 58px; line-height: 57px; letter-spacing: 4px; color: var(--ink);
  }
  .chart { position: absolute; }
  .growth-chart { left: 260px; top: 300px; width: 440px; height: 220px; }
  .trend-chart { left: 250px; top: 600px; width: 450px; height: 170px; }
  .chart text { font-family: "Open Sans", sans-serif; }
  .trend-caption {
    position: absolute; left: 282px; top: 782px; width: 410px;
    font-family: "Open Sans", sans-serif; font-size: 13.5px; line-height: 15px; color: var(--purple);
  }
  .world-map {
    position: absolute; left: 270px; top: 905px; width: 425px; height: 215px;
    background: radial-gradient(ellipse at 50% 50%, var(--purple) 0%, rgba(126,74,145,.75) 55%, rgba(126,74,145,0) 75%);
  }
  .slide-title {
    position: absolute; left: 0; right: 0; top: 1138px; padding-left: 40px; text-align: center;
    font-family: "Archivo", sans-serif; font-stretch: 110%; font-size: 52px; color: var(--ink);
  }
</style>
</head>
<body>
<main class="slide">
  <div class="side-artwork" role="img" aria-label="Faint purple illustration of lungs and airways"></div>
  <div class="side-dots"><span></span><span></span><span></span><span></span><span></span></div>

  <div class="brand"><span class="brand-square"></span>Brook Medical</div>

  <ol class="agenda">
    <li>1.TEXT</li>
    <li>2.TEXT</li>
    <li>3.TEXT</li>
    <li>4.TEXT</li>
  </ol>

  <svg class="chart growth-chart" viewBox="0 0 440 220">
    <path d="M0 215 Q90 205 110 195 L110 215Z" fill="var(--slate)"/>
    <path d="M110 195 Q170 180 220 160 L220 215 L110 215Z" fill="var(--green)"/>
    <path d="M220 160 Q280 135 320 100 L320 215 L220 215Z" fill="var(--orange)"/>
    <path d="M320 100 Q390 50 435 0 L435 215 L320 215Z" fill="var(--red)"/>
    <g stroke-width="2">
      <line x1="60" y1="22" x2="60" y2="205" stroke="var(--slate)"/>
      <line x1="175" y1="22" x2="175" y2="180" stroke="var(--green)"/>
      <line x1="285" y1="22" x2="285" y2="130" stroke="var(--orange)"/>
      <line x1="395" y1="22" x2="395" y2="60" stroke="var(--red)"/>
    </g>
    <g font-size="14" text-anchor="middle">
      <text x="60" y="15" fill="var(--slate)">13%</text>
      <text x="175" y="15" fill="var(--green)">31%</text>
      <text x="285" y="15" fill="var(--orange)">45%</text>
      <text x="395" y="15" fill="var(--red)">77%</text>
    </g>
  </svg>

  <svg class="chart trend-chart" viewBox="0 0 450 170">
    <g stroke="var(--grid)" stroke-dasharray="3 3">
      <line x1="35" y1="20" x2="445" y2="20"/><line x1="35" y1="50" x2="445" y2="50"/>
      <line x1="35" y1="80" x2="445" y2="80"/><line x1="35" y1="110" x2="445" y2="110"/>
      <line x1="35" y1="140" x2="445" y2="140"/>
    </g>
    <line x1="35" y1="20" x2="35" y2="168" stroke="var(--purple)"/>
    <line x1="35" y1="168" x2="445" y2="168" stroke="var(--purple)"/>
    <g font-size="11" fill="var(--purple)" text-anchor="end">
      <text x="30" y="24">100%</text><text x="30" y="172">0%</text>
    </g>
    <polyline fill="none" stroke="var(--orange)" stroke-width="3"
      points="40,160 80,100 120,70 160,110 200,60 240,90 280,50 320,105 360,60 400,80 435,20"/>
    <polyline fill="none" stroke="var(--red)" stroke-width="3"
      points="40,165 80,150 120,160 160,120 200,140 240,95 280,130 320,110 360,140 400,100 435,60"/>
    <g fill="var(--paper)" stroke-width="3">
      <g stroke="var(--orange)">
        <circle cx="80" cy="100" r="5"/><circle cx="120" cy="70" r="5"/><circle cx="160" cy="110" r="5"/>
        <circle cx="200" cy="60" r="5"/><circle cx="240" cy="90" r="5"/><circle cx="280" cy="50" r="5"/>
        <circle cx="320" cy="105" r="5"/><circle cx="360" cy="60" r="5"/><circle cx="400" cy="80" r="5"/>
        <circle cx="435" cy="20" r="5"/>
      </g>
      <g stroke="var(--red)">
        <circle cx="80" cy="150" r="5"/><circle cx="160" cy="120" r="5"/><circle cx="240" cy="95" r="5"/>
        <circle cx="320" cy="110" r="5"/><circle cx="400" cy="100" r="5"/><circle cx="435" cy="60" r="5"/>
      </g>
    </g>
  </svg>

  <p class="trend-caption">Lorem ipsum dolor sit amet, consectetur adipiscing elit, sed do eiusmod tempor incididunt ut labore et dolore magna aliqua.</p>

  <div class="world-map" role="img" aria-label="Purple world map with percentage markers 24%, 71%, 33% and 57%"></div>

  <h1 class="slide-title">PRINT SLIDE</h1>
</main>
</body>
</html>
```